Tidewolf Charters - An Alaskan Fishing Charter needs brochure/logo

We need a design for a brochure to advertise our Charter Fishing business. We have two boats and take tourists to fish for Halibut, King Salmon, and other fish. We also do several sight seeing trips for whales, sea lions, waterfalls, eagles, etc...
Website is HookaTidewolf.com - Promo is a free trip to those who catch largest fish of the season.
We need a whole brand including a picture of the Kraken (whatever that may be) and pictures of local scenery that we can provide.
Updates

Reason: Due to the number of people working on this project and the changes needed to be made, we have decided to extend the timeline.

Target Market(s)

Tourists visiting Haines, Alaska or looking for Charter Fishing in Alaska

Industry/Entity Type

Business

Logo Text

TIDEWOLF CHARTERS

Requirements
Must have
• A logo with picture of Kraken. (our Kraken does not have to be the typical octopus looking Kraken, but we are using the term "Kraken" to mean the largest fish of the year.
Nice to have
• Full Color attractive brochure with catchy logo (supposed to be part of project).
• Pictures of local scenery and catches (we will provide).
• Texts. We included a self drawn sketch of the Kraken and a Halibut as well as other pictures which are copyright protected and are intended only as ideas.

```html
<!DOCTYPE html>
<html lang="en">
<head>
<meta charset="utf-8">
<title>Tidewolf Charters Brochure</title>
<link href="https://fonts.googleapis.com/css2?family=Questrial&family=Rubik:ital,wght@1,900&family=Archivo+Black&display=swap" rel="stylesheet">
<style>
:root{
  --stage:#4a4c4e;
  --ink:#050809;
  --deep:#0b2a30;
  --teal:#1fb8c8;
  --aqua:#39d6e0;
  --white:#f2f6f7;
  --red:#e0321c;
  --orange:#f0a020;
  --ring-gold:#eaa21c;
  --ring-red:#b8281a;
  --box:rgba(0,0,0,.86);
}
*{margin:0;padding:0;box-sizing:border-box}
html,body{width:1200px;height:1200px;overflow:hidden;background:var(--stage)}
body{position:relative;font-family:"Questrial",sans-serif;color:var(--white)}
.sheet{position:absolute;left:302px;width:664px;height:516px;display:flex;overflow:hidden}
.sheet--outside{top:64px}
.sheet--inside{top:630px}
.sheet__art{position:absolute;inset:0;
  background:
   radial-gradient(ellipse at 85% 10%,var(--aqua) 0%,rgba(31,184,200,.6) 22%,transparent 50%),
   radial-gradient(ellipse at 45% 0%,rgba(31,184,200,.75) 0%,transparent 40%),
   radial-gradient(ellipse at 90% 95%,rgba(31,150,170,.55) 0%,transparent 35%),
   linear-gradient(160deg,var(--deep) 0%,#061316 45%,var(--ink) 100%)}
.panel{position:relative;width:221px;height:100%;text-align:center;border-right:1px solid rgba(0,0,0,.35)}
.panel:last-child{border-right:none}
.heading{font-family:"Rubik",sans-serif;font-weight:900;font-style:italic;color:var(--red);line-height:1;letter-spacing:-.5px}
.box{background:var(--box);border-radius:14px;position:absolute}
.bold{font-family:"Archivo Black",sans-serif;font-weight:400}

/* outside */
.reserve .heading{position:absolute;top:112px;left:0;right:0;font-size:22px}
.reserve .box{top:132px;left:12px;right:12px;height:104px;border-radius:0 0 14px 14px;padding:16px 10px 0;font-size:8.5px;line-height:1.6}
.reserve .box .bold{font-size:10px}
.reserve .big-phone{position:absolute;top:252px;left:0;right:0;font-size:22px}
.contact .heading{position:absolute;top:106px;left:0;right:0;font-size:22px;z-index:1}
.contact .box{top:124px;left:14px;right:14px;height:290px;padding:28px 4px 0;font-size:12px;line-height:1.25}
.contact dt{margin-top:13px}
.contact dt:first-child{margin-top:0}
.contact dd{font-family:"Archivo Black",sans-serif;font-size:11px}
.contact dd.small{font-size:8px;line-height:1.9}
.brand{position:absolute;left:10px;right:10px;display:flex;flex-direction:column;align-items:center;gap:5px;font-family:"Questrial",sans-serif;color:var(--red);font-size:30px;line-height:1}
.brand__mark{width:42px;height:42px;border-radius:50%;background:var(--red)}
.brand__url{font-size:8px;color:var(--white);margin-top:2px}
.cover .brand{top:64px}
.cover .intro{position:absolute;top:290px;left:18px;right:18px;font-size:8.4px;line-height:1.6;text-align:justify}
.cover .cta{display:block;text-align:center;font-family:"Archivo Black",sans-serif;font-size:11px;letter-spacing:.5px;margin-top:2px}

/* inside */
.inside-head{position:absolute;top:28px;left:0;right:0;font-size:17px}
.inside-head span{display:block}
.inside-head span:first-child{color:var(--orange)}
.photo{position:absolute;border-radius:50%;overflow:hidden}
.photo--large{width:168px;height:168px;border:8px solid var(--ring-gold);top:80px;left:34px}
.photo--small{width:106px;height:106px;border:6px solid var(--ring-red);top:166px;left:114px}
.photo__fill{width:100%;height:100%}
.fill-catch{background:linear-gradient(180deg,#9ab8c8 0%,#5c7f8e 45%,#2d4a55 100%)}
.fill-catch-2{background:linear-gradient(180deg,#5fb2c2 0%,#3d8da0 55%,#d9dde0 100%)}
.fill-light{background:linear-gradient(180deg,#7a9ed0 0%,#c9d4de 40%,#3e5a4a 70%,#2a4456 100%)}
.fill-lion{background:linear-gradient(180deg,#b9c2c8 0%,#8a959c 55%,#d6d2c8 100%)}
.species{position:absolute;top:290px;left:14px;right:14px;font-size:11.5px;line-height:1.45}
.species .bold{font-size:13px}
.species p+p{margin-top:26px}
.tour-copy{position:absolute;top:290px;left:14px;right:14px;font-size:11.5px;line-height:1.42}
.tour-copy p+p{margin-top:16px}
.packages .heading{position:absolute;top:30px;left:0;right:0;font-size:22px;z-index:1}
.packages .box{top:48px;left:14px;right:10px;height:266px;padding:24px 6px 0;font-size:11px;line-height:1.6}
.packages h3{font-family:"Archivo Black",sans-serif;font-weight:400;font-size:12.5px;letter-spacing:-.3px;line-height:1.2;margin-bottom:4px}
.packages p+h3{margin-top:16px}
.packages .brand{top:340px;font-size:27px}
</style>
</head>
<body>

<section class="sheet sheet--outside" aria-label="Brochure outside">
  <div class="sheet__art" role="img" aria-label="Painted deep-sea background in teal and black with drifting red fish"></div>

  <div class="panel reserve">
    <h2 class="heading">Reservations:</h2>
    <div class="box">
      The easiest way to make reservations and pay is online at our website
      <span class="bold">www.HookaTidewolf.com</span>, however questions or help making reservations can be found by calling Captain Morrow at
    </div>
    <p class="heading big-phone">907-555-0148</p>
  </div>

  <div class="panel contact">
    <h2 class="heading">Contact Info:</h2>
    <dl class="box">
      <dt>Captain Dale Morrow</dt><dd>907-555-0148</dd>
      <dt>Home</dt><dd>907-555-0172</dd>
      <dt>Email</dt><dd>HookaTidewolf@mail.com</dd>
      <dt>Website:</dt><dd>www.HookaTidewolf.com</dd>
      <dt>Address:</dt><dd class="small">Tidewolf Charters, Box 4420, Haines,<br>Alaska 99827</dd>
    </dl>
  </div>

  <div class="panel cover">
    <div class="brand">
      <span class="brand__mark"></span>
      <span>TIDEWOLF<br>CHARTERS</span>
      <span class="brand__url">www.HookaTidewolf.com</span>
    </div>
    <p class="intro">At TIDEWOLF CHARTERS we understand the lure of catching the big one. We are dedicated to our clients as we fish the ocean depths in search of the TIDEWOLF! Each year's largest halibut receives the "TIDEWOLF AWARD" and their charter is on the house! Do you have what it takes to
      <span class="cta">HOOK A TIDEWOLF?</span></p>
  </div>
</section>

<section class="sheet sheet--inside" aria-label="Brochure inside">
  <div class="sheet__art" role="img" aria-label="Painted deep-sea background in teal and black with drifting red fish"></div>

  <div class="panel fishing">
    <h2 class="heading inside-head"><span>Alaskan Saltwater</span><span>Charter Fishing</span></h2>
    <div class="photo photo--large"><div class="photo__fill fill-catch" role="img" aria-label="Anglers on a boat holding large halibut"></div></div>
    <div class="photo photo--small"><div class="photo__fill fill-catch-2" role="img" aria-label="Angler holding a king salmon on the water"></div></div>
    <div class="species">
      <p><span class="bold">Targeted Species:</span><br>Halibut and King Salmon</p>
      <p><span class="bold">Other Catchable Species:</span> Rock Fish, Sockeye Salmon, Pink Salmon, Coho Salmon, Cod, Flounder, Wolf fish, Pollock, Shark</p>
    </div>
  </div>

  <div class="panel tour">
    <h2 class="heading inside-head"><span>Alaskan</span><span>Sightseeing Tour</span></h2>
    <div class="photo photo--large"><div class="photo__fill fill-light" role="img" aria-label="Lighthouse on a rocky island with snowy mountains"></div></div>
    <div class="photo photo--small"><div class="photo__fill fill-lion" role="img" aria-label="Sea lion resting on a rocky shore"></div></div>
    <div class="tour-copy">
      <p>Majestic mountain ranges jut straight out of the ocean on both sides of the Lynn Canal to produce several natural waterfalls and geological curiosities.</p>
      <p>Many wildlife species can be seen including: Bald Eagles, Humpback Whales, Orcas, Sea Lions, Seals, Brown and Black Bears, Moose, Wolf, various other species of birds.</p>
    </div>
  </div>

  <div class="panel packages">
    <h2 class="heading">Packages:</h2>
    <div class="box">
      <h3>½ Day Sightseeing<br>or Fishing:</h3>
      <p>(4 Hours) - Includes coffee, tea, water, snacks, and fish cleaning.</p>
      <h3>Full Day Sightseeing<br>or Fishing:</h3>
      <p>(8 Hours) – Go where the ½ day can't! Includes coffee, tea, water, snacks and a lunch on the water as well as fish cleaning services.</p>
    </div>
    <div class="brand">
      <span class="brand__mark"></span>
      <span>TIDEWOLF<br>CHARTERS</span>
      <span class="brand__url">www.HookaTidewolf.com</span>
    </div>
  </div>
</section>

</body>
</html>
```